Restaurant needs a vertical banner for fried catfish

Our restaurant is looking for an eye-catching 78.75in. x 36in. vertical physical banner ad for our fried catfish. Photos for The Skillet Shack will be provided as a reference but we will also accept anything similar to the photo. We will be using the following as our receptacle: https://www.plorvista.com/banner-stand/retractable-banner-stands/
The design must incorporate the following flavor texts:
Fried Catfish
Always Fresh!
Made from Scratch
Hand-cut Fillets
The Best Catfish in Texas
Served with fries, hush puppies, and a 32oz fountain drink
Also available by the pound!
The final design should be creative, professional, and eye-catching for customers.
Updates
Need extra days to review
Colors
Designer to choose colors to be used in the design.
Requirements
Must have
- We are open to any and all design elements, albeit the 'flavor texts' should not overpower, but complement The Skillet Shack photo. 'Fried Catfish' can be used in lieu of a main title/logo.
Nice to have
- Transparent or textured backgrounds that can encompass any or all part of the banner such as a cutting board, shadows, abstract, etc to show depth are a plus.
- Use of vectors or objects such as ribbons or shapes to encapsulate the 'flavor texts' are also encouraged.

```html
<!DOCTYPE html>
<html lang="en">
<head>
<meta charset="utf-8">
<title>The Skillet Shack – Fried Catfish Banner</title>
<link rel="stylesheet" href="https://fonts.googleapis.com/css2?family=Josefin+Sans:wght@400;600;700&family=Yellowtail&display=swap">
<style>
  :root {
    --stage: #e8e6e2;
    --teal: #2f6470;
    --teal-deep: #234f5a;
    --navy: #22284a;
    --navy-deep: #1a1f3b;
    --cream: #f2e8cf;
    --red: #b3333c;
    --cloth-red: #c23a44;
    --cloth-light: #efd3d3;
    --grey-text: #8d8fa3;
    --gold: #e2c27b;
    --white: #ffffff;
  }
  * { box-sizing: border-box; margin: 0; padding: 0; }
  html, body { width: 1079px; height: 1200px; overflow: hidden; background: var(--stage); }
  .canvas { position: relative; width: 1079px; height: 1200px; }
  .banner {
    position: absolute; left: 280px; top: 0; width: 520px; height: 1200px;
    background: var(--navy); overflow: hidden;
    font-family: "Josefin Sans", sans-serif;
  }
  .banner-shapes { position: absolute; inset: 0; }
  .tag-scratch {
    position: absolute; left: 18px; top: 70px; height: 36px; padding: 0 16px;
    background: var(--red); color: var(--white);
    font-weight: 600; font-size: 19px; letter-spacing: 1.5px; line-height: 40px;
    text-transform: uppercase;
  }
  .badge-pound {
    position: absolute; left: 411px; top: 56px; width: 110px; height: 110px;
    border-radius: 50%; background: var(--navy);
    border: 2px dotted var(--cream); outline: 4px solid var(--navy);
    display: flex; align-items: center; justify-content: center; text-align: center;
    color: var(--cream); font-weight: 600; font-size: 13px; line-height: 1.25;
    letter-spacing: 1px; text-transform: uppercase;
  }
  .brand-name {
    position: absolute; left: 0; right: 0; top: 420px; text-align: center;
    color: var(--cream); font-weight: 700; text-transform: uppercase; line-height: 0.95;
  }
  .brand-name .small { display: block; font-size: 34px; letter-spacing: 6px; }
  .brand-name .big { display: block; font-size: 78px; letter-spacing: 2px; }
  .tagline-fresh {
    position: absolute; left: 0; right: 0; top: 712px; text-align: center;
    color: var(--cream); font-size: 15px; font-weight: 600; letter-spacing: 2px;
    text-transform: uppercase;
  }
  .dish-title {
    position: absolute; left: 56px; top: 758px;
    color: var(--white); font-size: 40px; font-weight: 600; letter-spacing: 2px;
    text-transform: uppercase;
  }
  .ribbon-fillets {
    position: absolute; left: 56px; top: 824px; height: 46px; padding: 0 18px;
    background: var(--red); color: var(--white);
    font-size: 24px; font-weight: 600; letter-spacing: 1.5px; line-height: 52px;
    text-transform: uppercase;
  }
  .served-with {
    position: absolute; left: 56px; top: 912px;
    color: var(--grey-text); font-size: 27px; font-weight: 600; letter-spacing: 1.5px;
    line-height: 1.2; text-transform: uppercase;
  }
  .best-in-texas {
    position: absolute; left: 56px; top: 1030px;
    color: var(--gold); font-family: "Yellowtail", cursive; font-size: 38px;
  }
</style>
</head>
<body>
<main class="canvas">
  <section class="banner" aria-label="Fried catfish banner">
    <svg class="banner-shapes" width="520" height="1200" viewBox="0 0 520 1200">
      <defs>
        <linearGradient id="tealWall" x1="0" y1="0" x2="0" y2="1">
          <stop offset="0" stop-color="var(--teal-deep)"/>
          <stop offset="1" stop-color="var(--teal)"/>
        </linearGradient>
        <radialGradient id="platter" cx="0.5" cy="0.5" r="0.6">
          <stop offset="0" stop-color="#f0d08a"/>
          <stop offset="0.6" stop-color="#d9a54e"/>
          <stop offset="1" stop-color="#c7c4b6"/>
        </radialGradient>
        <linearGradient id="cloth" x1="0" y1="0" x2="1" y2="1">
          <stop offset="0" stop-color="var(--cloth-red)"/>
          <stop offset="1" stop-color="var(--cloth-light)"/>
        </linearGradient>
      </defs>
      <rect class="wall" x="0" y="0" width="520" height="420" fill="url(#tealWall)"/>
      <polygon class="cloth-left" role="img" aria-label="Red and white checkered tablecloth" points="0,380 150,380 120,560 0,800" fill="url(#cloth)"/>
      <polygon class="cloth-right" role="img" aria-label="Red and white checkered tablecloth" points="380,380 520,380 520,720 430,740" fill="url(#cloth)"/>
      <path class="logo-field" d="M20 360 H500 V690 Q260 740 20 690 Z" fill="var(--navy-deep)"/>
      <path class="lower-panel" d="M0 740 L520 700 V1200 H0 Z" fill="var(--navy)"/>
      <ellipse class="food-photo" role="img" aria-label="Plate of fried catfish fillets with hush puppies, fries and broccoli" cx="250" cy="300" rx="290" ry="130" fill="url(#platter)"/>
      <polygon class="cloth-bottom" role="img" aria-label="Red and white checkered tablecloth" points="0,1130 520,1080 520,1200 0,1200" fill="url(#cloth)"/>
    </svg>

    <div class="tag-scratch">Made from Scratch</div>
    <div class="badge-pound">Also<br>available<br>by the<br>pound!</div>

    <h1 class="brand-name"><span class="small">The</span><span class="big">Skillet<br>Shack</span></h1>
    <p class="tagline-fresh">Always Fresh!</p>

    <h2 class="dish-title">Fried Catfish</h2>
    <p class="ribbon-fillets">Hand-cut Fillets</p>
    <p class="served-with">Served with fries,<br>hush puppies,<br>&amp; 32oz fountain drink</p>
    <p class="best-in-texas">The Best Catfish in Texas</p>
  </section>
</main>
</body>
</html>
```